we are in the infrastructure business ( road construction ) and I need a billboard that I placed it at every project to illustrate that we worked there . We have the logo , I attached it , I just need an interesting design of the billboard.
The company s name is : Vextra Civil - I attached how to be written !
I don't need to write road construction business on it

Requirements
Must have
• Study the design of the logo I attached ( the sign with " KTP " is just an example !!
Nice to have
• the romanian flag but made into a special form ( I attached an Idea )

```html
<!DOCTYPE html>
<html lang="ro">
<head>
<meta charset="utf-8">
<title>Vextra Civil – Banner șantier</title>
<link rel="stylesheet" href="https://fonts.googleapis.com/css2?family=Jost:wght@500;600;700&display=swap">
<style>
  :root {
    --banner-bg: #f3f2ef;
    --ink: #161616;
    --decor-grey: #bdbdbd;
    --flag-blue: #1f5fae;
    --flag-yellow: #e9b92b;
    --flag-red: #e13b3f;
  }
  * { margin: 0; padding: 0; box-sizing: border-box; }
  html, body {
    width: 1200px;
    height: 900px;
    overflow: hidden;
    background: var(--banner-bg);
  }
  .banner {
    position: relative;
    width: 1200px;
    height: 900px;
    background: var(--banner-bg);
    font-family: "Jost", "Helvetica Neue", Arial, sans-serif;
    color: var(--ink);
  }
  .banner__decor {
    position: absolute;
    top: 0;
    right: 0;
    width: 527px;
    height: 530px;
    overflow: hidden;
  }
  .banner__decor-shape {
    position: absolute;
    right: -60px;
    top: -40px;
    width: 560px;
    height: 540px;
    border-radius: 50%;
    background: radial-gradient(circle at 55% 50%, #cdcdcd 0%, #dcdcda 55%, #e8e7e4 100%);
  }
  .banner__tagline {
    position: absolute;
    left: 69px;
    top: 462px;
    font-size: 29px;
    font-weight: 700;
    letter-spacing: 0.02em;
    text-transform: uppercase;
  }
  .flag-band {
    position: absolute;
    left: 0;
    top: 522px;
    display: flex;
    width: 627px;
    height: 15px;
  }
  .flag-band__stripe { flex: 1; }
  .flag-band__stripe--blue { background: var(--flag-blue); }
  .flag-band__stripe--yellow { background: var(--flag-yellow); }
  .flag-band__stripe--red { background: var(--flag-red); }
  .brand-name {
    position: absolute;
    left: 66px;
    top: 585px;
    font-size: 92px;
    font-weight: 600;
    letter-spacing: 0.14em;
    text-transform: uppercase;
    line-height: 1;
  }
</style>
</head>
<body>
  <main class="banner">
    <div class="banner__decor" role="img" aria-label="Large faint grey brand emblem used as a corner decoration">
      <div class="banner__decor-shape"></div>
    </div>

    <p class="banner__tagline">Construim încredere!</p>

    <div class="flag-band" aria-hidden="true">
      <span class="flag-band__stripe flag-band__stripe--blue"></span>
      <span class="flag-band__stripe flag-band__stripe--yellow"></span>
      <span class="flag-band__stripe flag-band__stripe--red"></span>
    </div>

    <h1 class="brand-name">Vextra Civil</h1>
  </main>
</body>
</html>
```